Postcard Design Project

private loan company where loans are funded by private individual investors.
This would be a postcard advertising for additional investors.

```html
<!DOCTYPE html>
<html lang="en">
<head>
<meta charset="utf-8">
<title>Summit Crest Lending – Investor Postcard</title>
<link href="https://fonts.googleapis.com/css2?family=Open+Sans:ital,wght@0,400;0,600;0,700;0,800;1,700&display=swap" rel="stylesheet">
<style>
  :root{
    --navy:#17398a;
    --red:#d1121d;
    --red-dark:#a80d16;
    --gold:#c8a02a;
    --white:#ffffff;
    --ink:#333333;
    --page:#ececec;
    --photo:#8f9aa6;
  }
  *{box-sizing:border-box;margin:0;padding:0}
  html,body{width:689px;height:1200px;overflow:hidden}
  body{background:var(--page);font-family:"Open Sans",Arial,sans-serif;position:relative}
  .card{position:absolute;left:30px;width:629px;height:420px;overflow:hidden;box-shadow:0 6px 18px rgba(0,0,0,.25)}
  .card--front{top:150px;background:var(--navy)}
  .card--back{top:630px;background:var(--white)}
  .card svg.shapes,.photo{position:absolute;left:0;top:0;width:629px;height:420px}

  .quote{position:absolute;left:250px;right:18px;top:16px;text-align:right;color:var(--white)}
  .quote__text{font-weight:800;font-size:12px;line-height:18px;text-transform:uppercase}
  .quote__author{font-size:11px;text-transform:uppercase;margin-top:2px}
  .quote__mark{font-size:22px;font-weight:800;line-height:0;vertical-align:-6px}

  .intro{position:absolute;left:330px;width:290px;top:146px;color:var(--white);font-size:10.6px;line-height:14.6px;text-align:center;white-space:nowrap}
  .intro em{font-weight:700}

  .contact{position:absolute;left:26px;color:var(--white)}
  .contact--web{top:346px;font-size:17px;display:flex;align-items:center;gap:12px}
  .contact--phone{top:374px;font-size:23px;font-weight:700;display:flex;align-items:center;gap:8px}

  .brand{position:absolute;color:var(--navy);font-weight:700;display:flex;align-items:center;gap:8px;white-space:nowrap}
  .brand__dot{width:14px;height:14px;border-radius:50%;background:var(--navy)}
  .brand--front{left:392px;top:362px;font-size:14px}
  .nmls{position:absolute;right:22px;top:386px;color:var(--red);font-size:9px;font-weight:700}
  .brand--back{left:282px;top:24px;font-size:10px}

  .invite{position:absolute;left:12px;top:12px;color:var(--white);font-size:9.2px;line-height:13.4px;white-space:nowrap}
  .invite strong{font-weight:700}
  .features{position:absolute;left:12px;top:122px;list-style:none;color:var(--white);font-size:9.2px;line-height:12px;white-space:nowrap}
  .features li{display:flex;gap:8px;margin-bottom:9px}
  .features svg{flex:none;margin-top:2px}
  .legal{position:absolute;left:12px;top:304px;color:var(--ink);font-size:9.2px;line-height:13.4px;white-space:nowrap}
  .call{position:absolute;left:12px;top:383px;color:var(--white);font-size:21px;font-weight:700}

  .stamp{position:absolute;left:529px;top:21px;width:76px;height:65px;border:1px solid #666}
  .address-line{position:absolute;left:414px;width:192px;height:1px;background:#777}
</style>
</head>
<body>

<section class="card card--front" aria-label="Postcard front">
  <svg class="shapes" viewBox="0 0 513 342" preserveAspectRatio="none" aria-hidden="true">
    <defs>
      <linearGradient id="silverFront" x1="0" y1="0" x2="1" y2="1">
        <stop offset="0" stop-color="#f4f4f5"/><stop offset=".6" stop-color="#c9cacd"/><stop offset="1" stop-color="#eeeeef"/>
      </linearGradient>
    </defs>
    <path d="M195,0 H513 V84 Q400,100 268,48 Q225,28 195,0 Z" fill="var(--red)"/>
    <path d="M205,6 Q250,40 290,58 Q400,104 513,90" fill="none" stroke="#e6e7ea" stroke-width="4"/>
    <path d="M0,268 Q160,292 300,278 Q420,262 513,238 V258 Q370,268 290,342 H0 Z" fill="var(--red)"/>
    <path d="M290,342 Q370,268 513,258 V342 Z" fill="url(#silverFront)"/>
    <path d="M288,342 Q368,266 513,256" fill="none" stroke="var(--red-dark)" stroke-width="2"/>
    <path d="M200,0 Q258,80 248,162 Q240,230 198,284" fill="none" stroke="#e6e7ea" stroke-width="5"/>
  </svg>
  <svg class="photo" viewBox="0 0 513 342" preserveAspectRatio="none" role="img" aria-label="Photo of a smiling family posing with outstretched arms on a sunny beach">
    <path d="M0,0 H197 Q254,80 244,162 Q236,228 195,282 Q100,288 0,268 Z" fill="var(--photo)"/>
  </svg>

  <blockquote class="quote">
    <p class="quote__text"><span class="quote__mark">“</span> He who earns and does not invest will<br>have to work for the rest of his life</p>
    <p class="quote__author">Elliot Marwood <span class="quote__mark">”</span></p>
  </blockquote>

  <p class="intro">As an experienced or recent California trust deed<br>investor I would like to invite you to join our email list<br>to receive our trust deed investment<br><em>Executive Summaries</em>.<br>These one-page summaries are emailed<br>when newly originated trust deed investments are<br>ready for review and funding. Summit Crest Lending,<br>Inc. has been originating privately funded or<br><em>“hard money”</em> loans in California since 2001.</p>

  <p class="contact contact--web">
    <svg width="14" height="14" viewBox="0 0 14 14" aria-hidden="true"><circle cx="7" cy="7" r="6" fill="none" stroke="#fff" stroke-width="1.3"/><ellipse cx="7" cy="7" rx="2.6" ry="6" fill="none" stroke="#fff" stroke-width="1"/><path d="M1,7 H13 M2,4 H12 M2,10 H12" stroke="#fff" stroke-width="1"/></svg>
    www.summitcrestlending.info
  </p>
  <p class="contact contact--phone">
    <svg width="18" height="18" viewBox="0 0 24 24" aria-hidden="true"><path d="M6.6 10.8a15 15 0 0 0 6.6 6.6l2.2-2.2a1 1 0 0 1 1-.25 11.4 11.4 0 0 0 3.6.57 1 1 0 0 1 1 1V20a1 1 0 0 1-1 1A17 17 0 0 1 3 4a1 1 0 0 1 1-1h3.5a1 1 0 0 1 1 1c0 1.25.2 2.45.57 3.57a1 1 0 0 1-.25 1z" fill="#fff"/></svg>
    (800) 555-0147
  </p>

  <p class="brand brand--front"><span class="brand__dot"></span>Summit Crest Lending, Inc.</p>
  <p class="nmls">NMLS # 482716</p>
</section>

<section class="card card--back" aria-label="Postcard back">
  <svg class="shapes" viewBox="0 0 513 342" preserveAspectRatio="none" aria-hidden="true">
    <defs>
      <linearGradient id="goldSwoosh" x1="0" y1="0" x2="0" y2="1">
        <stop offset="0" stop-color="#f0d77a"/><stop offset=".5" stop-color="var(--gold)"/><stop offset="1" stop-color="#9c7414"/>
      </linearGradient>
    </defs>
    <path d="M0,0 H178 Q214,40 228,92 H0 Z" fill="var(--red)"/>
    <path d="M0,92 H228 Q250,170 258,245 H0 Z" fill="var(--navy)"/>
    <path d="M0,308 H272 Q276,325 274,342 H0 Z" fill="var(--red)"/>
    <path d="M184,0 Q280,90 284,342" fill="none" stroke="url(#goldSwoosh)" stroke-width="6"/>
    <path d="M176,0 Q270,92 274,342" fill="none" stroke="#d5d6d9" stroke-width="1.5"/>
  </svg>

  <p class="brand brand--back"><span class="brand__dot"></span>Summit Crest Lending, Inc.</p>

  <p class="invite">If the monthly income offered by well-<br>secured trust deed investments is<br>attractive to you, please go to our website at:<br><strong>www.summitcrestlending.info</strong> to subscribe to our<br>email list and learn more about SCL and trust deed<br>investing. Our telephone number is <strong>1-800-555-0147</strong>.</p>

  <ul class="features">
    <li><svg width="7" height="7" viewBox="0 0 7 7" aria-hidden="true"><rect x=".5" y=".5" width="6" height="6" fill="none" stroke="#fff"/><path d="M1.5,3.5 L3,5 L5.8,1.5" fill="none" stroke="#fff"/></svg>Complete investor due diligence package.</li>
    <li><svg width="7" height="7" viewBox="0 0 7 7" aria-hidden="true"><rect x=".5" y=".5" width="6" height="6" fill="none" stroke="#fff"/><path d="M1.5,3.5 L3,5 L5.8,1.5" fill="none" stroke="#fff"/></svg>Currently originating non-owner occupied<br>residential loans (business purpose).</li>
    <li><svg width="7" height="7" viewBox="0 0 7 7" aria-hidden="true"><rect x=".5" y=".5" width="6" height="6" fill="none" stroke="#fff"/><path d="M1.5,3.5 L3,5 L5.8,1.5" fill="none" stroke="#fff"/></svg>Loan documents including note and deed of trust<br>show your name and vesting.</li>
    <li><svg width="7" height="7" viewBox="0 0 7 7" aria-hidden="true"><rect x=".5" y=".5" width="6" height="6" fill="none" stroke="#fff"/><path d="M1.5,3.5 L3,5 L5.8,1.5" fill="none" stroke="#fff"/></svg>Fund directly to the insuring title company.</li>
    <li><svg width="7" height="7" viewBox="0 0 7 7" aria-hidden="true"><rect x=".5" y=".5" width="6" height="6" fill="none" stroke="#fff"/><path d="M1.5,3.5 L3,5 L5.8,1.5" fill="none" stroke="#fff"/></svg>Utilizing leading industry loan and lender<br>document packages.</li>
    <li><svg width="7" height="7" viewBox="0 0 7 7" aria-hidden="true"><rect x=".5" y=".5" width="6" height="6" fill="none" stroke="#fff"/><path d="M1.5,3.5 L3,5 L5.8,1.5" fill="none" stroke="#fff"/></svg>Typical terms are for 3-7 years.</li>
    <li><svg width="7" height="7" viewBox="0 0 7 7" aria-hidden="true"><rect x=".5" y=".5" width="6" height="6" fill="none" stroke="#fff"/><path d="M1.5,3.5 L3,5 L5.8,1.5" fill="none" stroke="#fff"/></svg>Both purchase and refinance loans</li>
  </ul>

  <p class="legal">Summit Crest Lending, Inc. 1450 Canyon Vista Drive, Suite 210<br>Desert Springs CA 92201 CA Department of Real Estate –<br>Real Estate Broker License # 02947731 NMLS # 482716<br>Martin Hale CA Department of Real Estate – Real Estate<br>Broker License # 01583390 NMLS # 517604</p>

  <p class="call">Call Us:(800) 555-0147</p>

  <div class="stamp" aria-hidden="true"></div>
  <div class="address-line" style="top:209px"></div>
  <div class="address-line" style="top:250px"></div>
  <div class="address-line" style="top:292px"></div>
</section>

</body>
</html>
```